GUARANTEE PAY GIFT CARD DESIGN

This is a GIFT BONUS CARD

SIZE: 3.5INCH x 2INCH, 8.9cm x 5.1cm, DOUBLE SIDE
Orange must be used as an accent or primary colour.
#F37021, CMYK 0, 54, 86, 5

"BONUS CARD" AND "$20" MUST BE PART OF THE DESIGN.

Please see the attached logo
DO NOT use ribbons or gift box illustrations in the design.

***Terms and conditions must be on the back side of the card-
"No Cash Value. Card valid from 1/2/2024 to 3/31/2024. Valid for Riverside location only. Valid for Dine-in only. Not valid for online togo, delivery, or special events. "

Target Market(s)

40-60 YEARS OLD

Industry/Entity Type

Modern casual malaysian restaurant

Requirements
Must have
• ORANGE COLOUR, BONUS CARD, $20
Should not have
• Ribbons, gift box, CHOPSTICKS, BOWL, NOODLES, CHARATER ILLUSTRATIONS.

```html
<!DOCTYPE html>
<html lang="en">
<head>
<meta charset="utf-8">
<title>Lada Kitchen – $20 Bonus Card</title>
<link rel="stylesheet" href="https://fonts.googleapis.com/css2?family=Josefin+Sans:wght@400;600&family=Questrial&display=swap">
<style>
  :root {
    --orange: #f39322;
    --cream: #fbf0e6;
    --white: #ffffff;
    --backdrop: #2b2b2b;
    --ink-display: "Josefin Sans", sans-serif;
    --ink-body: "Questrial", sans-serif;
  }
  * { box-sizing: border-box; margin: 0; padding: 0; }
  html, body {
    width: 1200px; height: 959px; overflow: hidden;
    background: var(--backdrop);
  }
  .sheet {
    position: relative; width: 1200px; height: 959px;
    display: flex; align-items: center; justify-content: center; gap: 40px;
  }
  .card {
    position: relative; width: 520px; height: 297px;
    border-radius: 16px; background: var(--white); overflow: hidden;
  }

  /* ---------- back side ---------- */
  .card-back .rule {
    position: absolute; left: 0; right: 0; top: 112px; height: 3px; background: var(--orange);
  }
  .card-back .terms-band {
    position: absolute; left: 0; right: 0; top: 121px; bottom: 0; background: var(--orange);
  }
  .brand-disc {
    position: absolute; border-radius: 50%; background: var(--orange);
    display: flex; align-items: center; justify-content: center; text-align: center;
    color: var(--white); font-family: var(--ink-display); font-weight: 400;
    letter-spacing: 0.08em; line-height: 1.05;
  }
  .card-back .brand-disc {
    width: 136px; height: 136px; left: 192px; top: 22px;
    border: 4px solid var(--white); font-size: 22px;
  }
  .terms {
    position: absolute; left: 30px; right: 30px; top: 170px;
    text-align: center; color: var(--white); font-family: var(--ink-body);
  }
  .terms-title {
    display: inline-block; font-size: 19px; font-weight: 400;
    padding-bottom: 3px; border-bottom: 1.5px solid var(--white); margin-bottom: 10px;
  }
  .terms-body { font-size: 11.5px; line-height: 1.55; }

  /* ---------- front side ---------- */
  .card-front .value-band {
    position: absolute; left: 0; right: 0; top: 92px; height: 118px;
    background: var(--cream);
    border-top: 4px solid var(--orange); border-bottom: 4px solid var(--orange);
  }
  .card-front .brand-disc {
    width: 176px; height: 176px; left: 62px; top: 62px;
    border: 7px solid var(--white); font-size: 28px;
  }
  .offer {
    position: absolute; left: 270px; top: 104px; width: 220px;
    color: var(--orange); font-family: var(--ink-display); text-align: center;
  }
  .offer-amount { font-size: 80px; font-weight: 600; line-height: 0.95; }
  .offer-label { font-size: 22px; font-weight: 400; letter-spacing: 0.12em; }
</style>
</head>
<body>
<main class="sheet">

  <section class="card card-back" aria-label="Bonus card, back side">
    <div class="rule"></div>
    <div class="terms-band"></div>
    <div class="brand-disc">LADA<br>KITCHEN</div>
    <div class="terms">
      <h2 class="terms-title">Terms and conditions</h2>
      <p class="terms-body">"No Cash Value. Card valid from 1/2/2024 to 3/31/2024. Valid for Riverside location only.<br>Valid for Dine-in only. Not valid for online togo, delivery, or special events."</p>
    </div>
  </section>

  <section class="card card-front" aria-label="Bonus card, front side">
    <div class="value-band"></div>
    <div class="brand-disc">LADA<br>KITCHEN</div>
    <div class="offer">
      <div class="offer-amount">$20</div>
      <div class="offer-label">BONUS CARD</div>
    </div>
  </section>

</main>
</body>
</html>
```